Business Card Design

We need a new business card design for a company based in Brookvale, TX. We provide business consulting services in the information technology / services space. We like variations of the color blue, aqua, black, light tan, and white. Would like "cool" tones. The design should clearly communicate professionalism. Think outside the box - we don't want something "typical". Our company name is "Harlow Advisory, LLC".
Updates

Thank you all for your submissions. We have seen some very creative and inspired designs. We have made a decision and will be moving forward with that design. Appreciate all of the hard work.

Industry/Entity Type

Information Technology

Contact Information for Business Card

Megan Harlow Pruett
318 West Birchfield Run Dr.
Brookvale, TX 76418

```html
<!DOCTYPE html>
<html lang="en">
<head>
<meta charset="utf-8">
<title>Harlow Advisory, LLC — Business Card</title>
<link rel="stylesheet" href="https://fonts.googleapis.com/css2?family=Jost:wght@300;400;500&display=swap">
<style>
  :root {
    --backdrop: #e6e9ec;
    --card: #f7f7f7;
    --band-deep: #1cb0e8;
    --band-deep-edge: #38bdee;
    --band-light-top: #9fe2f9;
    --band-light-bottom: #5ccaf3;
    --ink: #16263a;
  }
  html, body {
    margin: 0;
    width: 1200px;
    height: 576px;
    overflow: hidden;
    background: var(--backdrop);
  }
  .stage {
    width: 1200px;
    height: 576px;
    display: flex;
    align-items: center;
    justify-content: center;
  }
  .business-card {
    position: relative;
    width: 700px;
    height: 400px;
    background: var(--card);
    box-shadow: 0 6px 22px rgba(0, 0, 0, 0.15);
    overflow: hidden;
    font-family: "Jost", "Futura", sans-serif;
    color: var(--ink);
  }
  .band {
    position: absolute;
    left: 0;
    right: 0;
    top: 118px;
    height: 176px;
    display: flex;
    justify-content: space-between;
  }
  .contact-block {
    width: 338px;
    height: 100%;
    background: linear-gradient(90deg, var(--band-deep) 0%, var(--band-deep-edge) 100%);
    border-radius: 0 88px 88px 0;
    box-sizing: border-box;
    padding: 22px 0 0 28px;
  }
  .contact-name {
    margin: 0;
    font-weight: 300;
    font-size: 25px;
    line-height: 1.2;
  }
  .contact-address {
    margin: 20px 0 0;
    font-style: normal;
    font-weight: 300;
    font-size: 19px;
    line-height: 1.2;
    white-space: nowrap;
  }
  .company-block {
    width: 336px;
    height: 100%;
    background: linear-gradient(180deg, var(--band-light-top) 0%, var(--band-light-bottom) 100%);
    border-radius: 88px 0 0 88px;
    box-sizing: border-box;
    padding: 0 0 0 28px;
    display: flex;
    align-items: center;
  }
  .company-name {
    margin: 0;
    font-weight: 500;
    font-size: 24px;
    letter-spacing: 0.3px;
    white-space: nowrap;
  }
</style>
</head>
<body>
  <main class="stage">
    <article class="business-card">
      <div class="band">
        <section class="contact-block">
          <h1 class="contact-name">Megan Harlow Pruett</h1>
          <address class="contact-address">
            318 West Birchfield Run Dr.<br>
            Brookvale, TX 76418
          </address>
        </section>
        <section class="company-block">
          <p class="company-name">Harlow Advisory, LLC</p>
        </section>
      </div>
    </article>
  </main>
</body>
</html>
```